Parent company of several different entertainment businesses needs urgent business card design

We need a business card design for key senior staff. The company name is "Bramblewick Leisure", with full legal name being Bramblewick Leisure Group Pte Ltd. No logo is required, just an update to existing design (which is a bit bland). Need to use a similar script font as the "Bramblewick" in attached. The "Entertainment" can be on a second line if required, with emphasis on the "Bramblewick". Will need to make a quick decision within 24hrs.
We operate in Asia, and Australia/NZ. Brands we work with include (www.hopvarle.example.au and www.quillmarsh-play.example and www.rendovaup.example). We will need to depict these brand logos on the back of the card. Require artwork file in eps so as can change names etc for additional staff. Thanks
Updates

Target Market(s)

Corporate target (This is the parent company, not the super fun entertainment outlets)

Industry/Entity Type

Business

Contact Information for Business Card

Name: Dorian Pellacott
Title: Executive Director
Email: dorian@bramblewick-leisure.example
Phone: +65 9000 0000
Address: 14 Fennick Rd, #05-03 Halvorne Plaza, Singapore 200000

Requirements
Should not have
• No picture logo required. Just use the company name, with emphasis on "Bramblewick"

```html
<!DOCTYPE html>
<html lang="en">
<head>
<meta charset="UTF-8">
<title>Bramblewick Leisure – Business Card</title>
<link rel="stylesheet" href="https://fonts.googleapis.com/css2?family=Courgette&family=Roboto:ital,wght@0,400;0,500;0,700;1,700&family=Lato:wght@400&display=swap">
<style>
  :root {
    --canvas-bg: #e4e4e4;
    --card-bg: #fbfbfb;
    --ink: #111111;
    --ink-soft: #555555;
    --rule: #cfcfcf;
    --rule-dark: #444444;
    --brand-red: #e2312f;
    --brand-blue: #1d8fd8;
    --brand-purple: #6a3aa0;
  }
  * { margin: 0; padding: 0; box-sizing: border-box; }
  html, body { width: 1200px; height: 960px; overflow: hidden; }
  body { background: var(--canvas-bg); position: relative; font-family: "Roboto", Arial, sans-serif; color: var(--ink); }

  .card { position: absolute; width: 601px; height: 343px; background: var(--card-bg); }
  .card--front { left: 314px; top: 113px; }
  .card--back { left: 311px; top: 472px; width: 600px; }

  .wordmark { position: absolute; text-align: center; }
  .wordmark__script { font-family: "Courgette", cursive; font-size: 42px; line-height: 1; color: var(--ink); display: block; }
  .wordmark__caption { font-family: "Lato", sans-serif; font-size: 14px; letter-spacing: 4.6px; color: var(--ink); display: block; margin-top: 6px; padding-left: 4px; }
  .card--front .wordmark { left: 26px; width: 244px; top: 138px; }
  .card--back .wordmark { left: 150px; width: 300px; top: 40px; }
  .card--back .wordmark__script { font-size: 46px; }
  .card--back .wordmark__caption { font-size: 15px; letter-spacing: 5px; }

  .divider { position: absolute; left: 283px; top: 85px; width: 1px; height: 182px; background: var(--rule); }

  .contact { position: absolute; left: 309px; top: 86px; }
  .contact__name { font-size: 20px; font-weight: 500; letter-spacing: 0.2px; line-height: 1.2; }
  .contact__title { font-size: 15px; font-weight: 500; line-height: 1.3; margin-top: 1px; }
  .contact__address { font-size: 14.5px; color: var(--ink-soft); line-height: 18px; margin-top: 7px; font-style: normal; }
  .contact__lines { list-style: none; margin-top: 9px; }
  .contact__lines li { font-size: 14.5px; color: var(--ink-soft); line-height: 19px; display: flex; align-items: center; }
  .contact__lines svg { width: 12px; height: 12px; margin-right: 10px; flex: none; fill: var(--ink); }

  .partners-heading { position: absolute; left: 76px; top: 132px; width: 427px; display: flex; align-items: center; }
  .partners-heading__rule { flex: 1; height: 1.5px; background: var(--rule-dark); }
  .partners-heading__text { font-family: "Courgette", cursive; font-size: 20px; padding: 0 4px; color: var(--ink); }

  .partners { position: absolute; left: 40px; top: 200px; width: 520px; display: flex; justify-content: space-between; }
  .partner { width: 170px; text-align: center; }
  .partner__mark { display: flex; align-items: center; justify-content: center; gap: 6px; height: 40px; font-size: 19px; font-weight: 700; color: var(--ink); }
  .partner__dot { width: 14px; height: 14px; border-radius: 50%; flex: none; }
  .partner__dot--red { background: var(--brand-red); }
  .partner__dot--blue { background: var(--brand-blue); }
  .partner__dot--purple { background: var(--brand-purple); }
  .partner__url { font-size: 12px; color: var(--ink-soft); margin-top: 12px; }

  .regions { position: absolute; left: 0; width: 100%; top: 296px; text-align: center; font-size: 13px; font-weight: 700; font-style: italic; }
</style>
</head>
<body>
  <section class="card card--front" aria-label="Business card front">
    <div class="wordmark">
      <span class="wordmark__script">Bramblewick</span>
      <span class="wordmark__caption">LEISURE</span>
    </div>
    <div class="divider"></div>
    <div class="contact">
      <h1 class="contact__name">DORIAN PELLACOTT</h1>
      <p class="contact__title">EXECUTIVE DIRECTOR</p>
      <address class="contact__address">14 Fennick Rd<br>#05-03 Halvorne Plaza<br>Singapore 200000</address>
      <ul class="contact__lines">
        <li><svg viewBox="0 0 24 24" aria-hidden="true"><path d="M6.6 10.8a15.2 15.2 0 0 0 6.6 6.6l2.2-2.2c.3-.3.7-.4 1-.2 1.1.4 2.3.6 3.6.6.6 0 1 .4 1 1V20c0 .6-.4 1-1 1C10.6 21 3 13.4 3 4c0-.6.4-1 1-1h3.5c.6 0 1 .4 1 1 0 1.3.2 2.5.6 3.6.1.3 0 .7-.2 1z"/></svg>+65 9000 0000</li>
        <li><svg viewBox="0 0 24 24" aria-hidden="true"><path d="M2 5h20v14H2z M4 7v.5l8 5 8-5V7l-8 5z" fill-rule="evenodd"/></svg>dorian@bramblewick-leisure.example</li>
        <li><svg viewBox="0 0 24 24" aria-hidden="true"><circle cx="12" cy="12" r="10"/><path d="M7 9c2-1 3 1 5 0s2 3 0 4-1 4-3 4M14 6c1 1 3 1 3 3s2 2 2 3" stroke="#fbfbfb" stroke-width="1.8" fill="none"/></svg>bramblewick-leisure.example</li>
      </ul>
    </div>
  </section>

  <section class="card card--back" aria-label="Business card back">
    <div class="wordmark">
      <span class="wordmark__script">Bramblewick</span>
      <span class="wordmark__caption">LEISURE</span>
    </div>
    <div class="partners-heading">
      <span class="partners-heading__rule"></span>
      <span class="partners-heading__text">Brands we work with</span>
      <span class="partners-heading__rule"></span>
    </div>
    <div class="partners">
      <div class="partner">
        <div class="partner__mark"><span class="partner__dot partner__dot--red"></span>HOPVARLE</div>
        <p class="partner__url">www.hopvarle.example.au</p>
      </div>
      <div class="partner">
        <div class="partner__mark"><span class="partner__dot partner__dot--blue"></span>QUILLMARSH</div>
        <p class="partner__url">www.quillmarsh-play.example</p>
      </div>
      <div class="partner">
        <div class="partner__mark"><span class="partner__dot partner__dot--purple"></span>RENDOVA UP</div>
        <p class="partner__url">www.rendovaup.example</p>
      </div>
    </div>
    <p class="regions">We operate in Asia, and Australia/NZ.</p>
  </section>
</body>
</html>
```